Business Card Design

I am selling Cruelty Free/not tested on animal products.
Ideally I would like pictures of rabbits/guinea pigs/Beagle(dog)/rat/mice, as these are the main creatures that are tested on.
Background of card Earth, clouds or rainbow.
Yes I am an animal activist.
My favorite colours are purple and green.

Industry/Entity Type

Business

Contact Information for Business Card

GENTLY FROM MEADOW
Cruelty Free Products
Maren Holtby
0483 529 714

```html
<!DOCTYPE html>
<html lang="en">
<head>
<meta charset="utf-8">
<title>Gently From Meadow – Business Card</title>
<link href="https://fonts.googleapis.com/css2?family=Cinzel:wght@500&family=Arimo:wght@400;700&display=swap" rel="stylesheet">
<style>
  :root {
    --stage: #eef0f3;
    --card-white: #ffffff;
    --sky-deep: #a9c6e6;
    --sky-mid: #cfe0f1;
    --sky-pale: #eef4fa;
    --brand-purple: #5a3f9a;
    --brand-green: #1e9a3a;
    --logo-green: #2f9d4a;
  }
  * { box-sizing: border-box; margin: 0; padding: 0; }
  html, body {
    width: 1200px;
    height: 900px;
    overflow: hidden;
    background: var(--stage);
  }
  .canvas {
    position: relative;
    width: 1200px;
    height: 900px;
  }
  .business-card {
    position: absolute;
    left: 100px;
    top: 140px;
    width: 1000px;
    height: 620px;
    border-radius: 44px;
    overflow: hidden;
    background: var(--card-white);
    box-shadow: 0 18px 40px rgba(0, 0, 0, 0.18);
  }
  .sky-backdrop {
    position: absolute;
    inset: 0 0 70px 0;
    background:
      radial-gradient(ellipse 40% 22% at 70% 18%, rgba(255,255,255,0.75), transparent 70%),
      radial-gradient(ellipse 35% 18% at 20% 40%, rgba(255,255,255,0.6), transparent 70%),
      radial-gradient(ellipse 45% 20% at 80% 55%, rgba(255,255,255,0.6), transparent 70%),
      linear-gradient(180deg, var(--sky-deep) 0%, var(--sky-mid) 40%, var(--sky-pale) 70%, var(--card-white) 88%);
  }
  .footer-band {
    position: absolute;
    left: 0;
    right: 0;
    bottom: 0;
    height: 70px;
    background: var(--brand-purple);
  }
  .brand-mark {
    position: absolute;
    left: 150px;
    top: 150px;
    width: 170px;
    height: 170px;
    border-radius: 50%;
    background: var(--logo-green);
  }
  .brand-divider {
    position: absolute;
    left: 350px;
    top: 100px;
    width: 3px;
    height: 270px;
    background: var(--brand-purple);
  }
  .brand-name {
    position: absolute;
    left: 374px;
    top: 168px;
    font-family: "Cinzel", "Times New Roman", serif;
    font-weight: 500;
    font-size: 46px;
    color: var(--brand-purple);
    white-space: nowrap;
  }
  .brand-tagline {
    position: absolute;
    left: 378px;
    top: 240px;
    font-family: "Arimo", Arial, sans-serif;
    font-weight: 700;
    font-size: 29px;
    letter-spacing: 2.5px;
    color: var(--brand-green);
    white-space: nowrap;
  }
  .contact {
    position: absolute;
    left: 0;
    right: 0;
    top: 400px;
    text-align: center;
    font-family: "Arimo", Arial, sans-serif;
  }
  .contact-name {
    font-weight: 700;
    font-size: 34px;
    color: var(--brand-green);
    line-height: 1.3;
  }
  .contact-phone {
    font-weight: 400;
    font-size: 40px;
    color: var(--brand-purple);
    letter-spacing: 1px;
    line-height: 1.3;
  }
</style>
</head>
<body>
  <main class="canvas">
    <section class="business-card">
      <div class="sky-backdrop" role="img" aria-label="Soft blue sky with white clouds"></div>
      <div class="brand-mark" aria-hidden="true"></div>
      <div class="brand-divider" aria-hidden="true"></div>
      <h1 class="brand-name">GENTLY FROM MEADOW</h1>
      <p class="brand-tagline">Cruelty Free Products</p>
      <div class="contact">
        <p class="contact-name">Maren Holtby</p>
        <p class="contact-phone">0483 529 714</p>
      </div>
      <div class="footer-band" aria-hidden="true"></div>
    </section>
  </main>
</body>
</html>
```